mno school poster design and change logo name

We already have a logo which only needs to be slightly modified with "school".
We also have two advertising faces, a girl and a boy, which should be on our poster.
Important key data:

bilingual D/E small classes
daycare
private kindergarten
private school from 2024

Poster size: 268,5 x 128 cm
We need logo sizes in different sizes
also for T-shirts.
Attached also a old poster

Target Market(s)

new clients

Colors
0094D4
00A9DD
6FCCEA
C7EBF8
E9F6FB
59FF00
82FF00
B8FF75
E3FFCB
F4FFEA
FFC000
F8CF3A
FAE287
FDF2CF
FEFAEE
F0912C
F2A743
F7CA91
FBE8D2
FDF5EE

```html
<!DOCTYPE html>
<html lang="de">
<head>
<meta charset="utf-8">
<title>mno school – Poster</title>
<link rel="stylesheet" href="https://fonts.googleapis.com/css2?family=Fredoka:wght@400;500;600;700&family=Oswald:wght@400;500&display=swap">
<style>
  :root{
    --page:#ffffff;
    --cream:#fdfbf0;
    --band-blue:#0a6be0;
    --ink-blue:#2b4db8;
    --star-blue:#3a9de8;
    --red:#c8332b;
    --pink:#e83e8c;
    --orange:#ef5a24;
    --green-text:#1bb800;
    --bar-pink:#f54487;
    --splash-green:#7ed957;
    --splash-red:#ef2b3d;
    --splash-yellow:#ffd400;
    --white:#ffffff;
  }
  *{margin:0;padding:0;box-sizing:border-box}
  html,body{width:1200px;height:1200px;overflow:hidden;background:var(--page)}
  .canvas{position:relative;width:1200px;height:1200px;background:var(--page)}
  .poster{position:absolute;left:0;top:314px;width:1200px;height:571px;background:var(--cream);overflow:hidden;font-family:"Fredoka",sans-serif}
  .splash{position:absolute;border-radius:0 0 50% 50%}
  .splash-green-left{left:0;top:0;width:130px;height:136px;background:radial-gradient(circle at 40% 30%,var(--splash-green) 55%,transparent 72%)}
  .splash-red{left:843px;top:0;width:125px;height:96px;background:radial-gradient(circle at 50% 25%,var(--splash-red) 52%,transparent 72%)}
  .splash-yellow{left:972px;top:0;width:165px;height:86px;background:radial-gradient(circle at 50% 20%,var(--splash-yellow) 52%,transparent 72%)}
  .splash-green-right{left:1062px;top:0;width:138px;height:150px;background:radial-gradient(circle at 65% 25%,var(--splash-green) 52%,transparent 72%)}
  .headline{position:absolute;left:112px;top:29px;width:706px;height:85px;background:var(--band-blue);color:var(--white);font-weight:500;font-size:25px;line-height:40px;padding:5px 0 0 20px;white-space:nowrap;overflow:hidden;z-index:2}
  .offer-list{position:absolute;left:44px;top:143px;list-style:none;font-family:"Oswald",sans-serif;font-weight:400;font-size:34px;line-height:39px;letter-spacing:.4px}
  .offer-list li{display:flex;align-items:center;height:39px}
  .offer-list svg{width:20px;height:20px;margin-right:10px;flex:none}
  .offer-bilingual{color:var(--red)}
  .offer-daycare{color:var(--pink)}
  .offer-kindergarten{color:var(--ink-blue)}
  .offer-school{color:var(--orange)}
  .register-badge{position:absolute;left:488px;top:162px;width:130px;height:130px;border-radius:50%;background:var(--orange);color:var(--white);font-size:24px;font-weight:500;line-height:34px;display:flex;align-items:center;justify-content:center;text-align:center;z-index:3}
  .brand-box{position:absolute;left:739px;top:126px;width:224px;height:157px;border:3px solid var(--star-blue);border-radius:10px;background:var(--cream);display:flex;align-items:center;justify-content:center;gap:10px;z-index:3}
  .brand-dot{width:20px;height:20px;border-radius:50%;background:var(--pink)}
  .brand-name{font-weight:700;font-size:28px;color:var(--red)}
  .age-info{position:absolute;left:130px;top:317px;width:250px;text-align:center;color:var(--green-text);font-size:21px;font-weight:600;line-height:23.6px}
  .contact{position:absolute;left:0;width:510px;text-align:center;color:var(--ink-blue);font-size:23px;font-weight:500;white-space:nowrap}
  .contact-phone{top:432px}
  .contact-address{top:464px}
  .web-bar{position:absolute;left:0;top:509px;width:1200px;height:62px;background:var(--bar-pink)}
  .web-address{position:absolute;left:77px;top:13px;color:var(--white);font-size:26px;font-weight:600}
  .photo{position:absolute;z-index:1}
  .photo-girl{left:450px;top:272px;width:440px;height:299px;background:linear-gradient(180deg,#d9b08a 0%,#e8c2a2 45%,#f3e8df 100%);border-radius:40% 40% 0 0}
  .photo-boy{left:855px;top:266px;width:345px;height:305px;background:linear-gradient(180deg,#c99671 0%,#d8a887 45%,#3fb3e0 100%);border-radius:40% 40% 0 0}
</style>
</head>
<body>
<div class="canvas">
  <section class="poster">
    <div class="splash splash-green-left" role="img" aria-label="Green paint splash"></div>
    <div class="splash splash-red" role="img" aria-label="Red paint splash"></div>
    <div class="splash splash-yellow" role="img" aria-label="Yellow paint splash"></div>
    <div class="splash splash-green-right" role="img" aria-label="Green paint splash"></div>

    <div class="headline">Bei Uns lernen ALLE Kinder Speilend Einfach In<br>Kürzester Zeit Englisch Wie Eine 2. Muttersprache</div>

    <ul class="offer-list">
      <li class="offer-bilingual"><svg viewBox="0 0 20 20"><path d="M10 0 12 8 20 10 12 12 10 20 8 12 0 10 8 8Z" fill="var(--star-blue)"/></svg>BILINGUAL D/E SMALL CLASSES</li>
      <li class="offer-daycare"><svg viewBox="0 0 20 20"><path d="M10 0 12 8 20 10 12 12 10 20 8 12 0 10 8 8Z" fill="var(--star-blue)"/></svg>DAYCARE</li>
      <li class="offer-kindergarten"><svg viewBox="0 0 20 20"><path d="M10 0 12 8 20 10 12 12 10 20 8 12 0 10 8 8Z" fill="var(--star-blue)"/></svg>PRIVATE KINDERGARTEN</li>
      <li class="offer-school"><svg viewBox="0 0 20 20"><path d="M10 0 12 8 20 10 12 12 10 20 8 12 0 10 8 8Z" fill="var(--star-blue)"/></svg>PRIVATE SCHOOL FROM 2024</li>
    </ul>

    <div class="register-badge">Register<br>Now</div>

    <div class="brand-box">
      <span class="brand-dot"></span>
      <span class="brand-name">mno school</span>
    </div>

    <p class="age-info">Kinderkrippe &amp; hort<br>AB 3. lebensmonat<br>Biz Zum<br>12.lebensjahr</p>

    <p class="contact contact-phone">+41 79 555 20 48</p>
    <p class="contact contact-address">Lindenweg 12, 8050 Sonnfeld</p>

    <div class="web-bar"><span class="web-address">www.mno-daycare.ch</span></div>

    <div class="photo photo-girl" role="img" aria-label="Smiling girl with long brown hair holding up paint-covered hands"></div>
    <div class="photo photo-boy" role="img" aria-label="Laughing boy in a blue t-shirt reaching out with colourful painted hands"></div>
  </section>
</div>
</body>
</html>
```